serious, thorough, light and simple - that's my advice and mediations

My business card should combine my logo (uploaded file) and my homepage (https://fellor-mediation.webnestsite.com).

Contact Information for Business Card

Name: Sabine Fellor di Vanti
Phone: 076 412 58 94
mail: sfellor@postkiv.ch
web: www.fellor-di-vanti.ch

```html
<!DOCTYPE html>
<html lang="de">
<head>
<meta charset="utf-8">
<title>Visitenkarte – Sabine Fellor di Vanti</title>
<link rel="stylesheet" href="https://fonts.googleapis.com/css2?family=Questrial&display=swap">
<style>
  :root {
    --backdrop: #8a6a48;
    --card: #ffffff;
    --gold: #a8844f;
    --green: #1e6a3c;
    --icon-ring: #3b4f9a;
  }
  * { margin: 0; padding: 0; box-sizing: border-box; }
  html, body {
    width: 900px; height: 1200px; overflow: hidden;
    background: var(--backdrop);
    font-family: "Questrial", "Century Gothic", sans-serif;
  }
  .canvas { position: relative; width: 900px; height: 1200px; }
  .card {
    position: absolute; left: 80px; width: 733px; height: 428px;
    background: var(--card); border-radius: 28px;
  }
  .card--front { top: 128px; }
  .card--back { top: 647px; }

  .brand { position: absolute; display: flex; flex-direction: column; }
  .brand__name { color: var(--gold); font-weight: 400; white-space: nowrap; line-height: 1; }
  .brand__tagline { color: var(--green); white-space: nowrap; line-height: 1; }

  .card--front .brand { left: 0; right: 0; top: 190px; align-items: center; padding-left: 14px; }
  .card--front .brand__name { font-size: 52px; }
  .card--front .brand__tagline { font-size: 12.5px; letter-spacing: 0.22em; margin-top: 26px; }

  .card--back .brand { left: 64px; top: 68px; align-items: flex-start; }
  .card--back .brand__name { font-size: 29px; }
  .card--back .brand__tagline { font-size: 8.5px; letter-spacing: 0.2em; margin-top: 16px; }

  .contact { position: absolute; right: 34px; top: 274px; text-align: right; }
  .contact__name { color: var(--gold); font-size: 22px; margin-bottom: 14px; }
  .contact__list { list-style: none; }
  .contact__item {
    display: flex; justify-content: flex-end; align-items: center;
    color: var(--green); font-size: 15.5px; height: 31px;
  }
  .contact__icon { width: 26px; height: 26px; margin-left: 12px; flex: none; }
</style>
</head>
<body>
<main class="canvas">
  <section class="card card--front" aria-label="Vorderseite">
    <div class="brand">
      <span class="brand__name">Wege im Dialog</span>
      <span class="brand__tagline">ZUHÖREN, VERSTEHEN, LÖSEN</span>
    </div>
  </section>

  <section class="card card--back" aria-label="Rückseite">
    <div class="brand">
      <span class="brand__name">Wege im Dialog</span>
      <span class="brand__tagline">ZUHÖREN, VERSTEHEN, LÖSEN</span>
    </div>

    <div class="contact">
      <p class="contact__name">Sabine Fellor di Vanti</p>
      <ul class="contact__list">
        <li class="contact__item">076 412 58 94
          <svg class="contact__icon" viewBox="0 0 26 26" aria-hidden="true">
            <circle cx="13" cy="13" r="11.5" fill="none" stroke="var(--icon-ring)" stroke-width="1.6"/>
            <path d="M9 7.5l2 .3 1 2.8-1.4 1.2a8 8 0 0 0 3.6 3.6l1.2-1.4 2.8 1-.1 2.2c-.2.6-1 1-1.8.9A10 10 0 0 1 8 9.3c-.1-.8.3-1.6 1-1.8z" fill="var(--gold)"/>
          </svg>
        </li>
        <li class="contact__item">sfellor@postkiv.ch
          <svg class="contact__icon" viewBox="0 0 26 26" aria-hidden="true">
            <circle cx="13" cy="13" r="11.5" fill="none" stroke="var(--icon-ring)" stroke-width="1.6"/>
            <rect x="7" y="9" width="12" height="8.5" rx="1" fill="var(--gold)"/>
            <path d="M7.5 9.5l5.5 4.5 5.5-4.5" fill="none" stroke="#fff" stroke-width="1.1"/>
          </svg>
        </li>
        <li class="contact__item">www.fellor-di-vanti.ch
          <svg class="contact__icon" viewBox="0 0 26 26" aria-hidden="true">
            <circle cx="13" cy="13" r="11.5" fill="none" stroke="var(--icon-ring)" stroke-width="1.6"/>
            <circle cx="13" cy="13" r="6.5" fill="var(--gold)"/>
            <path d="M6.5 13h13M13 6.5v13M13 6.5c-3 3.5-3 9.5 0 13M13 6.5c3 3.5 3 9.5 0 13" fill="none" stroke="#fff" stroke-width="0.9"/>
          </svg>
        </li>
      </ul>
    </div>
  </section>
</main>
</body>
</html>
```